Toy Company Needs a Web Site For a New Toy

We need a web site for a new toy called "Zippa Roller". The bike is a plastic, non motorized ride on toy for kids ages 1.5 - 5 years of age. The bike is being launched in three colors, red, blue and pink, though we may include a black option too.

For the web site we want something bold and colorful that communicates fun, therefore NO dull colors like black or grey. Nothing too cluttered. We want the site to attract the attention of kids but also give the parents a sense of confidence in our professionalism as a trustworthy toy company. The home page should focus on the bike, with different views of the bike and a small write-up on some of its key features. We would also like the home page to have a video of the bike in play. A obvious link to the shopping basket must be present as well. The site must include a shopping basket and ordering system.

Attached is a screenshot of a site that has the colourfulness and playfulness that we are looking for. Please have a look.

The bike images attached are renderings from the CAD software, actual high res photos will be used when the site is developed.

The product logo is attached and MUST be used on the site. It must be BOLD and can be incorporated into the actual website design.

The site pages are:
Home
Gallery
Buy
Contact

Competitors:
www.brimvalekids.example
www.quorvaride.example
I do not like either of their sites.

We only have one product at this time, so the site is to be focused on that product, not a whole catalog of products. It is really a single product with the ability to purchase.
Updates

Project Deadline Extended
Reason: I am extending this competition in order to give me more time to review each design and provide the feedback that the designers deserve.

Target Market(s)

Parents, children ages 1.5 - 5.

Industry/Entity Type

It Company

Colors
0555a3
eb1f27
9bcb3c
faed22
f78f20
f37022
e34197
a6459a
6b449b

Requirements
Must have
• Please use the logo attached, but feel free to use different colors.
Should not have
• Dull colors like black and grey

```html
<!DOCTYPE html>
<html lang="en">
<head>
<meta charset="utf-8">
<title>Zippa Roller</title>
<link rel="stylesheet" href="https://fonts.googleapis.com/css2?family=Alfa+Slab+One&family=Indie+Flower&display=swap">
<style>
  :root {
    --red: #e5322f;
    --red-dark: #d42a27;
    --cream: #fdf8e2;
    --blush: #fbe9ea;
    --white: #ffffff;
    --frame: #fff6d6;
    --text-grey: #7a7a7a;
    --soft-grey: #9a9a9a;
    --line-grey: #dddddd;
    --field-grey: #f1f1f1;
    --cart-blue: #3aa6d8;
    --ink: #1f1f1f;
  }
  * { box-sizing: border-box; margin: 0; padding: 0; }
  html, body { width: 1200px; height: 1057px; overflow: hidden; }
  body {
    position: relative;
    background: var(--cream);
    font-family: Arial, Helvetica, sans-serif;
  }
  .backdrop-pattern {
    position: absolute; inset: 0;
    background: radial-gradient(circle at 20% 30%, #fbe3ec 0, transparent 40%),
                radial-gradient(circle at 80% 75%, #fbe3ec 0, transparent 40%),
                var(--cream);
  }
  .hero-band {
    position: absolute; left: 0; top: 93px; width: 1200px; height: 462px;
    background: var(--red);
  }
  .header-top {
    position: absolute; left: 211px; top: 0; width: 778px; height: 93px;
    background: rgba(255,255,255,0.75);
  }
  .header-bar {
    position: absolute; left: 211px; top: 93px; width: 778px; height: 97px;
    background: var(--blush);
  }
  .brand-badge {
    position: absolute; left: 209px; top: 10px; width: 180px; height: 180px;
    border-radius: 50%; background: var(--red);
    border: 7px solid var(--white);
    display: flex; align-items: center; justify-content: center; text-align: center;
  }
  .brand-badge__name {
    font-family: 'Alfa Slab One', serif; color: var(--white);
    font-size: 24px; line-height: 26px;
  }
  .nav-ring {
    position: absolute; left: 391px; top: 93px; width: 96px; height: 96px;
    border-radius: 50%; border: 5px solid var(--white);
  }
  .main-nav a {
    position: absolute; top: 135px; transform: translateX(-50%);
    font-family: 'Alfa Slab One', serif; font-size: 12px; color: var(--red);
    text-decoration: none; letter-spacing: 0.3px;
  }
  .order-button {
    position: absolute; left: 867px; top: 8px; width: 116px; height: 29px;
    background: var(--red); border-radius: 5px; color: var(--white);
    font-family: 'Alfa Slab One', serif; font-size: 12px;
    display: flex; align-items: center; justify-content: center;
  }
  .cart-link { position: absolute; left: 872px; top: 103px; width: 110px; }
  .cart-link__title {
    font-family: 'Indie Flower', cursive; font-size: 22px; color: var(--ink); line-height: 24px;
  }
  .cart-link__count {
    display: flex; align-items: center; gap: 5px; margin-top: 1px;
    font-family: 'Indie Flower', cursive; font-size: 20px; color: var(--cart-blue); line-height: 22px;
  }
  .hero-title {
    position: absolute; left: 209px; top: 240px;
    font-family: 'Alfa Slab One', serif; font-size: 24px; color: var(--white);
  }
  .hero-copy {
    position: absolute; left: 214px; top: 297px; width: 350px;
    font-family: 'Indie Flower', cursive; font-size: 20px; line-height: 29px; color: var(--white);
  }
  .buy-button {
    position: absolute; left: 209px; top: 430px; width: 108px; height: 33px;
    background: var(--white); color: var(--red);
    font-family: 'Alfa Slab One', serif; font-size: 12px;
    display: flex; align-items: center; justify-content: center; gap: 6px;
  }
  .hero-photo {
    position: absolute; left: 585px; top: 200px; width: 400px; height: 286px;
    border: 7px solid var(--frame);
    background: linear-gradient(180deg, #3f6b2a 0%, #6a8a4a 45%, #5c5f62 70%, #3d4248 100%);
  }
  .content-card {
    position: absolute; left: 209px; top: 508px; width: 776px; height: 494px;
    background: var(--white); border-radius: 8px; border: 1px solid var(--red);
  }
  .section-title {
    position: absolute; font-family: 'Alfa Slab One', serif; font-size: 12px; letter-spacing: 0.2px;
  }
  .section-title--red { color: var(--red); }
  .section-title--grey { color: var(--soft-grey); }
  .body-copy {
    position: absolute; font-size: 9px; line-height: 11.5px; color: var(--text-grey);
  }
  .product-thumb {
    position: absolute; left: 35px; top: 150px; width: 127px; height: 95px;
    background: linear-gradient(180deg, #4f7a3a 0%, #6f8f55 50%, #8a8f8a 100%);
  }
  .column-divider {
    position: absolute; left: 492px; top: 28px; width: 1px; height: 323px; background: var(--line-grey);
  }
  .signup-field {
    position: absolute; left: 509px; top: 86px; width: 157px; height: 29px;
    background: var(--field-grey); font-size: 8px; color: #aaa; padding: 10px 13px;
  }
  .signup-submit {
    position: absolute; left: 666px; top: 86px; width: 60px; height: 29px;
    background: #d6d6d6; display: flex; align-items: center; justify-content: center;
  }
  .share-row { position: absolute; left: 509px; top: 194px; display: flex; gap: 6px; }
  .share-pill { display: flex; align-items: center; gap: 2px; font-size: 8px; }
  .share-pill__action {
    border: 1px solid #c8c8c8; border-radius: 2px; padding: 1px 4px; background: #f4f4f4; color: #333;
  }
  .share-pill__action--orange { background: #ef5a3a; border-color: #ef5a3a; color: var(--white); }
  .share-pill__count { border: 1px solid #d0d0d0; border-radius: 2px; padding: 1px 4px; color: #555; background: var(--white); }
  .follow-row { position: absolute; left: 510px; top: 268px; display: flex; gap: 7px; }
  .follow-dot { width: 22px; height: 22px; border-radius: 50%; background: linear-gradient(#b5b5b5, #7e7e7e); }
  .footer-badge {
    position: absolute; left: 11px; top: 389px; width: 44px; height: 44px;
    border-radius: 50%; border: 2px solid var(--ink);
    display: flex; align-items: center; justify-content: center; text-align: center;
    font-family: 'Alfa Slab One', serif; font-size: 7px; line-height: 8px; color: var(--ink);
  }
  .footer-rule { position: absolute; left: 77px; top: 412px; width: 673px; height: 1px; background: var(--line-grey); }
  .footer-links { position: absolute; left: 77px; top: 430px; font-size: 7.5px; color: var(--soft-grey); }
  .footer-links span { margin: 0 7px; }
  .footer-copy { position: absolute; right: 25px; top: 432px; font-size: 7.5px; color: var(--soft-grey); }
</style>
</head>
<body>
  <div class="backdrop-pattern" role="img" aria-label="Playful pattern of flowers and bubbles"></div>
  <div class="hero-band"></div>

  <header>
    <div class="header-top"></div>
    <div class="header-bar"></div>
    <a class="order-button">ORDER NOW</a>
    <div class="brand-badge"><span class="brand-badge__name">ZIPPA<br>ROLLER</span></div>
    <div class="nav-ring"></div>
    <nav class="main-nav">
      <a style="left:440px">HOME</a>
      <a style="left:542px">PRODUCT</a>
      <a style="left:632px">HOME</a>
      <a style="left:734px">CONTACT</a>
    </nav>
    <div class="cart-link">
      <div class="cart-link__title">YOUR CART</div>
      <div class="cart-link__count">
        <svg width="30" height="22" viewBox="0 0 30 22" aria-hidden="true">
          <path d="M1 3h5l4 12h14l3-9H8" fill="none" stroke="#1f1f1f" stroke-width="2.5" stroke-linejoin="round"/>
          <circle cx="12" cy="19" r="2" fill="#1f1f1f"/><circle cx="22" cy="19" r="2" fill="#1f1f1f"/>
        </svg>
        <span>5 items</span>
      </div>
    </div>
  </header>

  <section class="hero">
    <h1 class="hero-title">ZIPPA ROLLER</h1>
    <p class="hero-copy">Lorem Ipsum is simply dummy text of the printing and typesetting industry. Lorem Ipsum has been the industry's standard dummy text ever since the 1500</p>
    <a class="buy-button">
      <svg width="22" height="17" viewBox="0 0 30 22" aria-hidden="true">
        <path d="M1 3h5l4 12h14l3-9H8" fill="none" stroke="#1f1f1f" stroke-width="2.5" stroke-linejoin="round"/>
        <circle cx="12" cy="19" r="2" fill="#1f1f1f"/><circle cx="22" cy="19" r="2" fill="#1f1f1f"/>
      </svg>
      BUY NOW
    </a>
    <div class="hero-photo" role="img" aria-label="Silver ride-on toy bike with red wheels on a park path"></div>
  </section>

  <main class="content-card">
    <h2 class="section-title section-title--red" style="left:35px;top:40px">WELCOME TO OUR WEBSITE</h2>
    <p class="body-copy" style="left:35px;top:84px;width:445px">Lorem Ipsum is simply dummy text of the printing and typesetting industry. Lorem Ipsum has been the industry's standard dummy text ever since the 1500s, when an unknown printer took a galley of type and scrambled it to make a type specimen book.</p>
    <div class="product-thumb" role="img" aria-label="Blue ride-on toy bike on grass"></div>
    <p class="body-copy" style="left:178px;top:148px;width:303px">Lorem Ipsum is simply dummy text of the printing and typesetting industry. Lorem Ipsum has been the industry's standard dummy text ever since the 1500s, when an unknown printer took a galley of type and scrambled it to make a type specimen book.</p>

    <div class="column-divider"></div>

    <h2 class="section-title section-title--grey" style="left:509px;top:40px">SIGN UP FOR DISCOUNT</h2>
    <div class="signup-field">email@example.com</div>
    <div class="signup-submit">
      <svg width="22" height="14" viewBox="0 0 22 14" aria-hidden="true">
        <rect x="1" y="1" width="20" height="12" rx="1" fill="#f3f3f3" stroke="#9a9a9a"/>
        <path d="M1 1l10 7 10-7" fill="none" stroke="#9a9a9a"/>
      </svg>
    </div>
    <p class="body-copy" style="left:509px;top:125px;width:220px;font-size:7.5px;line-height:9px;color:#a5a5a5">Lorem Ipsum is simply dummy text of the printing and typesetting industry</p>

    <h2 class="section-title section-title--grey" style="left:509px;top:163px">LIKE ZIPPA ROLLER</h2>
    <div class="share-row">
      <div class="share-pill"><span class="share-pill__action">Like</span><span class="share-pill__count">3k</span></div>
      <div class="share-pill"><span class="share-pill__action">Post</span><span class="share-pill__count">316</span></div>
      <div class="share-pill"><span class="share-pill__action">+1</span><span class="share-pill__count">56</span></div>
      <div class="share-pill"><span class="share-pill__action share-pill__action--orange">Share</span><span class="share-pill__count">4.6K</span></div>
    </div>

    <h2 class="section-title section-title--grey" style="left:510px;top:233px">FOLLOW US ZIPPA ROLLER</h2>
    <div class="follow-row">
      <span class="follow-dot"></span><span class="follow-dot"></span><span class="follow-dot"></span><span class="follow-dot"></span>
    </div>

    <footer>
      <div class="footer-badge">ZIPPA<br>ROLLER</div>
      <div class="footer-rule"></div>
      <div class="footer-links">Home<span>|</span>About Us<span>|</span>Privacy Policy<span>|</span>Terms</div>
      <div class="footer-copy">2013. ZIPPA ROLLER. All right reserved</div>
    </footer>
  </main>
</body>
</html>
```